Navelo Partnering Business Card

Hello everyone. We need a business card design that would match our logo and the theme we're trying to have for Navelo that you can find on our website and/or Corvapage page

```html
<!DOCTYPE html>
<html lang="en">
<head>
<meta charset="utf-8">
<title>Navelo Partnering Business Card</title>
<link href="https://fonts.googleapis.com/css2?family=Oswald:wght@600&family=Work+Sans:wght@400;600&display=swap" rel="stylesheet">
<style>
  :root {
    --stage: #1f1f1f;
    --card-dark: #311d58;
    --card-light: #47326e;
    --ink: #ffffff;
  }
  * { box-sizing: border-box; margin: 0; padding: 0; }
  html, body { width: 1200px; height: 900px; overflow: hidden; }
  body {
    background: var(--stage);
    font-family: "Work Sans", sans-serif;
    color: var(--ink);
    display: flex;
    flex-direction: column;
    align-items: center;
    justify-content: center;
    gap: 44px;
  }
  .card {
    width: 660px;
    height: 377px;
    position: relative;
    background: linear-gradient(200deg, var(--card-light) 0%, var(--card-dark) 60%);
  }
  .card-front {
    display: flex;
    flex-direction: column;
    align-items: center;
  }
  .brand {
    margin-top: 138px;
    display: flex;
    align-items: center;
    gap: 12px;
    font-weight: 600;
    font-size: 54px;
    letter-spacing: 0.5px;
  }
  .brand-dot {
    width: 16px; height: 16px;
    border-radius: 50%;
    background: var(--ink);
  }
  .front-url {
    position: absolute;
    bottom: 44px;
    font-size: 14px;
    letter-spacing: 0.6px;
  }
  .identity {
    position: absolute;
    top: 140px;
    left: 40px;
    width: 250px;
    text-align: right;
  }
  .person-name {
    font-family: "Oswald", sans-serif;
    font-weight: 600;
    font-size: 38px;
    line-height: 1;
    letter-spacing: 0.5px;
    text-transform: uppercase;
    white-space: nowrap;
  }
  .person-role {
    font-size: 17px;
    margin-top: 4px;
    padding-right: 10px;
  }
  .divider {
    position: absolute;
    top: 140px;
    left: 308px;
    width: 2px;
    height: 76px;
    background: var(--ink);
  }
  .contacts {
    position: absolute;
    top: 142px;
    left: 330px;
    list-style: none;
    font-size: 17px;
    line-height: 25px;
    letter-spacing: 0.3px;
  }
  .contacts li { display: flex; align-items: center; gap: 10px; }
  .contacts svg { width: 12px; height: 12px; flex: none; }
  .address {
    position: absolute;
    left: 40px;
    bottom: 50px;
    font-size: 18px;
    letter-spacing: 0.4px;
  }
</style>
</head>
<body>
  <section class="card card-front">
    <div class="brand"><span class="brand-dot"></span>Navelo</div>
    <p class="front-url">www.navelopartnering.com</p>
  </section>

  <section class="card card-back">
    <div class="identity">
      <h1 class="person-name">Daniel Reyes</h1>
      <p class="person-role">Founder</p>
    </div>
    <div class="divider"></div>
    <ul class="contacts">
      <li>
        <svg viewBox="0 0 12 12" fill="none" stroke="#fff" stroke-width="1.3"><path d="M3 1.5 L4.5 3.5 L3.6 4.8 Q5 7.5 7.2 8.4 L8.5 7.5 L10.5 9 L9.5 10.5 Q4 10 1.5 3 Z"/></svg>
        555-014-2287
      </li>
      <li>
        <svg viewBox="0 0 12 12" fill="none" stroke="#fff" stroke-width="1.2"><rect x="1" y="2.5" width="10" height="7"/><path d="M1 2.5 L6 6.5 L11 2.5"/></svg>
        info@navelopartnering.com
      </li>
      <li>
        <svg viewBox="0 0 12 12" fill="none" stroke="#fff" stroke-width="1.1"><circle cx="6" cy="6" r="5"/><ellipse cx="6" cy="6" rx="2.2" ry="5"/><path d="M1 6 H11 M2 3.3 H10 M2 8.7 H10"/></svg>
        www.navelopartnering.com
      </li>
    </ul>
    <p class="address">2470 Harbor Ln. Coral Bend, FL 33012</p>
  </section>
</body>
</html>
```